WP website design (Volkamp)

We need a wordpress design for an established auction and real estate company based in Kansas. The winning design will incorporate a professional color scheme with company logo in a clean layout. The design needs to consider that this will be developed on a responsive theme. Colors are blue and gray, with perhaps an accent/highlight color.

Industry/Entity Type

Real Estate

Font styles to use
Serif
Sans Serif

Colors

Designer to choose colors to be used in the design.

Requirements
Must have
• Navigation:
1) Home 2) Auctions 3) Real Estate Listings 4) Buyers 5) Sellers 6) About Us 7) Contact Us 7) Brokers

Page will have slideshow, please use any stock real estate image initially. Homepage will have auctions - as at http://brindlegavelco.example/upcoming-auctions/. Footer will have smaller company logo and attached association logos.

Widgets:
1) email sign up 2) Social media (twitter, FB, youtube, RSS) 3) News & Events blog 4) Video Player
Nice to have
• demonstrate the drop-down menu styling, Past Auctions - under the main Auctions tab

```html
<!DOCTYPE html>
<html lang="en">
<head>
<meta charset="utf-8">
<title>Prairie Crest Volkamp Auction/Realty</title>
<link rel="stylesheet" href="https://fonts.googleapis.com/css2?family=Tinos:wght@400;700&family=PT+Sans:wght@400;700&display=swap">
<style>
:root{
  --navy:#0e3a5e;
  --navy-dark:#0a2a46;
  --blue:#1f5c8c;
  --link:#1d5a8a;
  --gray-bg:#e4e4e4;
  --panel:#d6d6d6;
  --card:#cfcfcf;
  --text:#555;
  --dark:#2a2a2a;
  --white:#fff;
}
*{box-sizing:border-box;margin:0;padding:0}
html,body{width:1200px;height:2332px;overflow:hidden}
body{position:relative;background:#ececec;font-family:"PT Sans",sans-serif;color:var(--text);font-size:15px}
.abs{position:absolute}
.serif{font-family:"Tinos",serif}
/* header */
.brand{left:70px;top:22px;width:210px;text-align:center;color:var(--navy)}
.brand .name{font-family:"Tinos",serif;font-size:38px;line-height:40px}
.brand .sub{font-size:16px;line-height:18px;color:#555;margin-top:8px}
.social{display:flex;gap:8px}
.social span{width:30px;height:30px;border-radius:50%;background:#9a9a9a;display:block}
.social span:last-child{background:var(--navy)}
.search{left:950px;top:82px;width:202px;height:34px;background:#fff;border:1px solid #ccc;border-radius:3px;padding:8px 14px;color:#aaa;font-size:14px}
.search svg{position:absolute;right:10px;top:8px}
.nav{left:50px;top:130px;width:1104px;height:56px;background:linear-gradient(#1f5a88,#0c3558);display:flex;z-index:2;box-shadow:0 2px 4px rgba(0,0,0,.3)}
.nav a{flex:auto;color:#fff;text-decoration:none;font-size:14px;letter-spacing:1px;text-align:center;line-height:56px;border-right:1px solid rgba(255,255,255,.15)}
.nav a:last-child{border:0}
/* hero */
.hero{left:0;top:152px;width:1200px;height:558px;background:linear-gradient(#5f88c0 0%,#b6c9dd 30%,#c4895a 52%,#6d4a2e 68%,#355a2b 78%,#2b6a86 88%,#0f3f5e 100%)}
.welcome{left:412px;top:212px;color:#fff;font-family:"Tinos",serif}
.welcome .small{font-size:19px}
.welcome .big{font-size:48px;letter-spacing:2px;line-height:50px}
.welcome p{font-size:15px;line-height:16px;width:380px}
.dots{left:568px;top:561px;display:flex;gap:8px}
.dots span{width:14px;height:14px;border-radius:50%;background:#ddd;border:2px solid #fff}
.dots span:first-child{background:var(--blue)}
.lightband{left:0;top:710px;width:1200px;height:338px;background:#e6e6e6}
/* info panel */
.panel{left:178px;top:592px;width:852px;height:456px;background:#dedede;border-radius:4px}
.col-head{height:40px;display:flex;background:linear-gradient(#1f5a88,#0c3558);color:#fff;font-family:"Tinos",serif;font-size:17px;letter-spacing:1px}
.col-head i{width:58px;background:#444;display:flex;align-items:center;justify-content:center;clip-path:polygon(0 0,100% 0,82% 100%,0 100%)}
.col-head b{flex:1;font-weight:400;text-align:center;line-height:40px}
.about{left:194px;top:607px;width:249px}
.photo-team{margin-top:10px;width:249px;height:122px;border:3px solid #fff;background:linear-gradient(#f0f0f0,#b8bcc2 50%,#2a2d33)}
.about p{font-size:15px;line-height:16px;letter-spacing:.5px;margin-top:8px}
.more{color:var(--link)}
.brokers{left:477px;top:607px;width:250px}
.broker{background:#cdcdcd;margin-top:10px;padding:10px;height:166px;position:relative}
.broker .pic{float:left;width:66px;height:68px;border:2px solid #fff;background:linear-gradient(#f2f2f2,#b9b3aa);margin-right:12px}
.broker h4{font-family:"Tinos",serif;color:var(--navy);font-weight:400;font-size:17px;border-bottom:1px solid #bbb;padding-bottom:4px;margin-bottom:6px}
.broker p{font-size:14px;line-height:16px;letter-spacing:.4px}
.btn-sm{display:inline-block;background:var(--navy);color:#fff;font-size:12px;padding:4px 10px;border-radius:2px;margin-top:4px}
.viewall{margin-top:10px;font-size:14px;letter-spacing:1px;text-decoration:underline;color:#666}
.contact{left:762px;top:607px;width:248px}
.cbox{background:#cdcdcd;margin-top:10px;padding:10px;display:flex;gap:12px;font-size:14px;line-height:15px}
.cbox svg{flex:none}
.news{background:#cdcdcd;margin-top:10px;padding:14px 28px;height:120px}
.news h5{font-family:"Tinos",serif;font-weight:400;font-size:16px;letter-spacing:1px;color:#333;text-align:center}
.news h5 span{color:var(--navy)}
.news .field{background:#fff;border:1px solid #bbb;height:30px;margin-top:8px;padding:6px 8px;color:#aaa;font-size:13px}
.news .btn{display:inline-block;margin-top:10px;background:var(--navy);color:#fff;padding:5px 22px;font-size:14px;letter-spacing:1px}
/* auctions */
.row{left:0;width:1200px}
.r1{top:1048px;height:282px;background:#f0f0f0}
.r2{top:1330px;height:238px;background:#ececec}
.r3{top:1568px;height:337px;background:#d9d9d9}
.sec-title{left:194px;top:1070px;width:830px;font-family:"Tinos",serif;font-size:24px;letter-spacing:1px;color:var(--navy);display:flex;align-items:center;gap:14px}
.sec-title span{color:#333}
.sec-title hr{flex:1;border:0;border-top:1px solid #ccc}
.auction{left:194px;width:820px}
.auction .img{width:284px;height:130px;border:2px solid #fff;background:linear-gradient(#8fb0c8,#c9bb95 45%,#4a6b35 70%,#5aa0b5)}
.auction .btns{position:absolute;left:6px;top:146px;display:flex;gap:8px}
.auction .btns span{border:1px solid #777;padding:6px 15px;font-size:14px;letter-spacing:1px;color:#444;background:#f5f5f5}
.auction .btns span.alt{border-color:var(--blue);color:var(--blue)}
.auction .txt{position:absolute;left:312px;top:0;width:508px}
.auction h3{font-family:"Tinos",serif;font-weight:400;font-size:19px;letter-spacing:1px;color:#333}
.auction p{font-size:14px;line-height:15px;letter-spacing:.3px;margin-top:6px}
.auction .loc{color:var(--navy);border-top:1px solid #ccc;border-bottom:1px solid #ccc;padding:4px 0;margin-top:10px;font-size:14px;letter-spacing:.5px}
.auction .dates{background:#ddd;margin-top:10px;padding:5px 10px;font-size:14px;line-height:17px;letter-spacing:.5px}
.allbtn{left:193px;top:1837px;width:204px;height:43px;background:linear-gradient(#1f5a88,#0c3558);color:#fff;text-align:center;line-height:43px;font-size:15px;letter-spacing:1px}
.divider{left:194px;top:1818px;width:834px;border-top:1px solid #bbb}
/* badges */
.badges{left:180px;top:1958px;width:830px;display:flex;justify-content:space-between;align-items:center}
.badges span{background:#2a2a2a;display:block}
/* footer */
.footer{left:0;top:2090px;width:1200px;height:198px;background:var(--navy)}
.fh{font-family:"Tinos",serif;color:#fff;font-size:20px;letter-spacing:2px;border-bottom:1px solid #3c6385;padding-bottom:8px}
.flinks{color:#fff;font-size:14px;letter-spacing:1px;line-height:26px}
.fbrand{left:850px;top:2120px;width:160px;text-align:center;color:#fff}
.fbrand .name{font-family:"Tinos",serif;font-size:26px;line-height:28px}
.fbrand .sub{font-size:13px;color:#ccd;margin-top:6px;line-height:15px}
.fsocial{left:866px;top:2232px}
.fsocial span{background:#ddd}
.copy{left:0;top:2288px;width:1200px;height:44px;background:#2b2b2b;color:#ccc;font-family:"Tinos",serif;font-size:13px;padding:14px 178px}
</style>
</head>
<body>
<div class="abs brand"><div class="name">Prairie Crest</div><div class="sub">Volkamp<br>Auction/Realty, LLC</div></div>
<div class="abs social" style="left:1007px;top:36px"><span></span><span></span><span></span><span></span></div>
<div class="abs search">Search<svg width="16" height="16" viewBox="0 0 16 16"><circle cx="6" cy="6" r="4.5" fill="none" stroke="#999" stroke-width="2"/><path d="M9.5 9.5L14 14" stroke="#999" stroke-width="2.5"/></svg></div>

<nav class="abs nav"><a>HOME</a><a>AUCTIONS</a><a>REAL ESTATE LISTINGS</a><a>BUYERS</a><a>SELLERS</a><a>ABOUT US</a><a>CONTACT US</a><a>BROKERS</a></nav>

<div class="abs hero" role="img" aria-label="Slideshow photo: modern luxury home at dusk with lit windows and a pool in front"></div>
<div class="abs welcome"><div class="small">Welcome to</div><div class="big">Prairie Crest</div><p>Lorem ipsum dolor sit amet, consectetur adipi-scing elit. Sed blandit nibh eu risus aliquet placerat. Nam ac feugiat sapien.</p></div>
<div class="abs dots"><span></span><span></span><span></span></div>
<div class="abs lightband"></div>

<div class="abs panel"></div>
<section class="abs about">
  <div class="col-head"><i><svg width="26" height="18" viewBox="0 0 26 18"><circle cx="8" cy="5" r="4" fill="#fff"/><circle cx="17" cy="5" r="4" fill="#fff"/><path d="M1 17c0-6 14-6 14 0zM11 17c0-6 14-6 14 0z" fill="#fff"/></svg></i><b>ABOUT US</b></div>
  <div class="photo-team" role="img" aria-label="Team photo of the company's agents standing together"></div>
  <p>Lorem ipsum dolor sitamet, ect ipiscing elit. Quisque non elit sit amet lorem ut luctus faucibus non elit.</p>
  <p>Lorem ipsum dolor sitamet, ect ipiscing elit. Quisque non elit sit amet lorem ut luctus faucibus non elitsit amet lorem ut luctus faucibus non elit.</p>
  <p class="more">Read more &raquo;</p>
</section>
<section class="abs brokers">
  <div class="col-head"><i><svg width="22" height="22" viewBox="0 0 22 22"><circle cx="11" cy="11" r="7" fill="none" stroke="#fff" stroke-width="4" stroke-dasharray="3 2.5"/><circle cx="11" cy="11" r="3" fill="#fff"/></svg></i><b>BROKERS</b></div>
  <div class="broker"><div class="pic" role="img" aria-label="Broker portrait"></div><h4>John Doe Smith</h4><p>ipsum dolor sit amet, consectetur taciti sociosqu ad litora tor per conubia nostra, pertos himenaeos</p><span class="btn-sm">Read More</span></div>
  <div class="broker"><div class="pic" role="img" aria-label="Broker portrait"></div><h4>Jane Marlow</h4><p>ipsum dolor sit amet, consectetur taciti sociosqu ad litora tor per conubia nostra, pertos himenaeos</p><span class="btn-sm">Read More</span></div>
  <div class="viewall">VIEW ALL BROKERS &raquo;</div>
</section>
<section class="abs contact">
  <div class="col-head"><i><svg width="20" height="20" viewBox="0 0 20 20"><path d="M4 2l4 4-2 2c1 3 3 5 6 6l2-2 4 4-3 3C8 18 2 12 1 5z" fill="#fff"/></svg></i><b>CONTACT US</b></div>
  <div class="cbox"><svg width="22" height="22"><circle cx="11" cy="11" r="10" fill="#333"/><path d="M9 6l5 5-5 5" stroke="#fff" stroke-width="2" fill="none"/></svg>youremail@mail.com</div>
  <div class="cbox"><svg width="22" height="22"><circle cx="11" cy="11" r="10" fill="#333"/><path d="M9 6l5 5-5 5" stroke="#fff" stroke-width="2" fill="none"/></svg><span>2218 HARVEST LANE<br>SUITE 4<br>SALINA, KS 67401</span></div>
  <div class="cbox"><svg width="22" height="22"><circle cx="11" cy="11" r="10" fill="#333"/><path d="M9 6l5 5-5 5" stroke="#fff" stroke-width="2" fill="none"/></svg><span>785.555.0142 TEL<br>785.555.0143 FAX<br>785.555.0199 MOBILE</span></div>
  <div class="news"><h5>NEWSLETTER <span>SIGNUP</span></h5><div class="field">Email Address</div><span class="btn">SUBMIT</span></div>
</section>

<div class="abs row r1"></div><div class="abs row r2"></div><div class="abs row r3"></div>
<h2 class="abs sec-title">UPCOMING <span>AUCTIONS</span><hr></h2>

<article class="abs auction" style="top:1108px">
  <div class="img" role="img" aria-label="Auction property: villa with pool and lounge chairs"></div>
  <div class="btns"><span>VIEW DETAILS</span><span class="alt">WATCH VIDEO</span></div>
  <div class="txt"><h3>TITLE OF THE PLACE GOES HERE</h3><p>Maecenas at orci quis leo gravida rhoncus eu et nulla. Vestibulum ante ipsum primis in faucibus orci luctus et ultrices posuere cubilia Curae; Nam diam nisi, faucibus ut dui in, orci luctus et ultrices posuere cubilia Curae; Nam diam nisi, faucibus ut dui in.</p><div class="loc">Location: P.O. Box 4410 Millbrook, KS 67456</div><div class="dates">Begins:&nbsp; Tuesday, March 04, 2014 at 10:00 AM EST<br>Ends:&nbsp; Tuesday, March 11, 2014 at 11:00 PM EST</div></div>
</article>
<article class="abs auction" style="top:1351px">
  <div class="img" role="img" aria-label="Auction property: villa with pool and lounge chairs"></div>
  <div class="btns"><span>VIEW DETAILS</span><span class="alt">WATCH VIDEO</span></div>
  <div class="txt"><h3>TITLE OF THE PLACE GOES HERE</h3><p>Maecenas at orci quis leo gravida rhoncus eu et nulla. Vestibulum ante ipsum primis in faucibus orci luctus et ultrices posuere cubilia Curae; Nam diam nisi, faucibus ut dui in, orci luctus et ultrices posuere cubilia Curae; Nam diam nisi, faucibus ut dui in.</p><div class="loc">Location: P.O. Box 4410 Millbrook, KS 67456</div><div class="dates">Begins:&nbsp; Tuesday, March 04, 2014 at 10:00 AM EST<br>Ends:&nbsp; Tuesday, March 11, 2014 at 11:00 PM EST</div></div>
</article>
<article class="abs auction" style="top:1593px">
  <div class="img" role="img" aria-label="Auction property: villa with pool and lounge chairs"></div>
  <div class="btns"><span>VIEW DETAILS</span><span class="alt">WATCH VIDEO</span></div>
  <div class="txt"><h3>TITLE OF THE PLACE GOES HERE</h3><p>Maecenas at orci quis leo gravida rhoncus eu et nulla. Vestibulum ante ipsum primis in faucibus orci luctus et ultrices posuere cubilia Curae; Nam diam nisi, faucibus ut dui in, orci luctus et ultrices posuere cubilia Curae; Nam diam nisi, faucibus ut dui in.</p><div class="loc">Location: P.O. Box 4410 Millbrook, KS 67456</div><div class="dates">Begins:&nbsp; Tuesday, March 04, 2014 at 10:00 AM EST<br>Ends:&nbsp; Tuesday, March 11, 2014 at 11:00 PM EST</div></div>
</article>
<div class="abs divider"></div>
<div class="abs allbtn">VIEW ALL AUCTIONS</div>

<div class="abs badges" aria-label="Association memberships">
  <span style="width:56px;height:64px"></span>
  <span style="width:120px;height:62px;background:none;border:3px solid #2a2a2a"></span>
  <span style="width:108px;height:46px"></span>
  <span style="width:74px;height:62px;border-radius:50%;background:none;border:3px solid #2a2a2a"></span>
  <span style="width:48px;height:56px"></span>
  <span style="width:46px;height:46px"></span>
  <span style="width:100px;height:40px"></span>
</div>

<footer class="abs footer"></footer>
<div class="abs" style="left:178px;top:2118px;width:360px"><div class="fh">QUICKLINKS</div>
  <div style="display:flex;gap:0;margin-top:8px"><div class="flinks" style="width:210px">&rsaquo; Home<br>&rsaquo; Auctions<br>&rsaquo; Real estate listings<br>&rsaquo; Buyers</div><div class="flinks">&rsaquo; Sellers<br>&rsaquo; About us<br>&rsaquo; Contact us<br>&rsaquo; Brokers</div></div></div>
<div class="abs" style="left:566px;top:2118px;width:196px"><div class="fh">INFORMATION</div><div class="flinks" style="margin-top:8px">&rsaquo; FAQ<br>&rsaquo; Sitemap<br>&rsaquo; Privacy Policy<br>&rsaquo; Terms &amp; Condition</div></div>
<div class="abs fbrand"><div class="name">Prairie Crest</div><div class="sub">Volkamp<br>Auction/Realty, LLC</div></div>
<div class="abs social fsocial"><span></span><span></span><span></span><span style="background:#5b8fc0"></span></div>
<div class="abs copy">Copyright 2014 · All rights reserved</div>
</body>
</html>
```